Bayline Pet Rehoming GALA

Hi ALL!
We need an 8.5 X 11 inch, one page flyer to include all the below copy plus 8 sponsoring logos at the very bottom.
Thank YOU!

Corvel Heights Pet GALA
(Fun for Animals In Rescue!)

Sunday, August 12, 2018
1 to 4:30 p.m.

Animal Education & Adoption Event
featuring:

BK Pet Shelter & Services Rabbits & Mice

Hilltop Browsing Sheep

Thankful Hounds Haven

Featherwell Finches & Larks

Comet Pup Haven

Marla’s Feline Haven

Marvel Pup Haven

Special Guest from 1-3 p.m.
BeeBop - SF's 1st Therapy Pig!
Instagram: @BEEBOP_BKHOG
Facebook: @BEEBOP THE HOG

Activities for Kids
Dog & Cat Toy Making with Greta Vossel Canine Coaching
Animal Mask Making with Tiny Crafters
Face-in-a-Hole Photo Fun with Hugo Marsh Canine Coaching

BK PSS FREE Giveaway!
First 75 attending families receive a FREE PSS Doggie Bag containing a dog water bottle, food, shampoo, toy, treats and blinking dog collar light.

Animal Tails

1 pm Wendell’s Nook Storytime

1:30 p.m. BeeBop the Therapy Pig

1:45 pm “Tuft the Saved Hog”
Read by Author Marnie Oakhurst

2 p.m. Wendell’s Nook Singalong

2:30 p.m. Featherwell Finch Haven

2:45 p.m. Quire Pages Storytime

3 pm Browsing Sheep Refuge

3:15 p.m. The Burrow Den Puppet Show

3:45 pm BK PSS Officer Tamsin

4 p.m. Wendell’s Nook Storytime

Font styles to use
Serif

Colors

Designer to choose colors to be used in the design.

Requirements
Must have
• pig, goat, 2 dogs, kitten, dove, bunny

```html
<!DOCTYPE html>
<html lang="en">
<head>
<meta charset="utf-8">
<title>Corvel Heights Pet GALA</title>
<link rel="stylesheet" href="https://fonts.googleapis.com/css2?family=Lilita+One&family=Montserrat:ital,wght@0,400;0,600;0,700;0,800;1,400&display=swap">
<style>
:root{
  --bg:#c8c9d9;
  --sky-top:#2f7fd6;
  --sky-mid:#8e93e0;
  --sky-low:#e3a6c9;
  --orange:#f39a1e;
  --green:#3aa83a;
  --blue:#1a9ad6;
  --blue-dark:#0f6fa8;
  --ink:#1b1b1b;
  --paper:#f4f4f6;
  --pale:#c5e3f2;
  --pink:#f09ab0;
}
*{margin:0;padding:0;box-sizing:border-box}
html,body{width:1200px;height:800px;overflow:hidden}
body{background:var(--bg);font-family:"Montserrat",sans-serif;color:var(--ink)}
.flyer{position:absolute;left:291px;top:0;width:618px;height:800px;background:var(--paper);overflow:hidden}
.header{position:absolute;left:0;top:0;width:618px;height:300px;background:linear-gradient(180deg,var(--sky-top),var(--sky-mid) 55%,var(--sky-low))}
.scene{position:absolute;left:0;top:176px;width:618px;height:104px;background:linear-gradient(180deg,#7fb7e8,#4caf4a 60%,#2f8a35)}
.art{position:absolute;border-radius:10px}
.art-bunny{left:190px;top:6px;width:54px;height:44px;background:#f2f2f7}
.art-dove{left:490px;top:8px;width:66px;height:40px;background:#f6f6fb}
.art-goat{left:480px;top:160px;width:118px;height:100px;background:linear-gradient(#b7713c,#8a4f27)}
.art-beagle{left:16px;top:176px;width:110px;height:92px;background:linear-gradient(#c98a4b,#7a4a23)}
.title{position:absolute;left:0;width:618px;top:56px;text-align:center;font-family:"Lilita One",sans-serif;font-size:60px;line-height:.95;color:var(--orange)}
.subtitle{position:absolute;left:0;width:618px;top:186px;text-align:center;font-family:"Lilita One",sans-serif;font-size:22px;color:var(--green)}
.curve{position:absolute;left:0;top:220px}
.date-pill{position:absolute;left:110px;top:262px;width:400px;height:38px;border-radius:19px;background:var(--blue);color:#fff;font-weight:800;font-size:16px;display:flex;align-items:center;justify-content:center;letter-spacing:.3px;border:3px solid #fff;box-shadow:0 0 0 2px var(--blue)}
.featuring{position:absolute;left:18px;top:318px;width:290px;text-align:center}
.featuring h2{font-size:12px;font-weight:800;white-space:nowrap}
.featuring .sub{font-size:11.5px;font-weight:700;margin-bottom:4px}
.featuring ul{list-style:none;display:grid;grid-template-columns:1fr 1fr;gap:2px 8px;font-size:9.8px;text-align:left;white-space:nowrap}
.art-dog{position:absolute;left:312px;top:340px;width:52px;height:60px;border-radius:12px;background:linear-gradient(#a76a3a,#e9e2dc)}
.guest{position:absolute;left:18px;top:428px;width:350px;height:130px}
.pig-badge{position:absolute;left:0;top:0;width:120px;height:120px;border-radius:50%;background:var(--pale);border:3px dashed var(--blue)}
.pig-art{position:absolute;left:13px;top:13px;width:88px;height:88px;border-radius:50%;background:var(--pink)}
.guest-text{position:absolute;left:130px;top:26px;width:220px;font-size:10.5px}
.guest-text strong{display:block;font-size:12px;font-weight:800;margin:3px 0 6px;white-space:nowrap}
.handle{display:flex;align-items:center;gap:5px;font-size:9.5px;margin-top:3px}
.dot{width:9px;height:9px;border-radius:2px;background:var(--blue-dark);display:inline-block}
.tab{display:inline-block;background:var(--blue);color:#fff;font-weight:700;font-size:13px;padding:4px 16px;border-radius:4px 18px 0 0}
.tails{position:absolute;left:372px;top:318px;width:236px}
.tails .rule{height:3px;background:var(--blue)}
.tails ol{list-style:none;margin-top:6px;font-size:10px;line-height:1.55}
.tails li{display:flex;gap:8px}
.tails .time{width:52px;flex:none;font-weight:600}
.tails .note{font-style:italic;color:#555;padding-left:60px}
.kids{position:absolute;left:18px;top:575px;width:370px}
.kids .rule{height:3px;background:var(--blue);width:580px}
.kids ul{list-style:none;margin-top:6px;font-size:10.5px;line-height:1.6;white-space:nowrap}
.kids li::before{content:"✔";margin-right:6px;font-weight:700}
.giveaway{position:absolute;left:0;top:680px;width:618px;height:120px;background:var(--blue);color:#fff}
.giveaway .big{position:absolute;left:20px;top:8px;font-weight:400;font-size:26px;line-height:.95}
.giveaway .big b{font-weight:800;font-size:32px;display:block}
.giveaway .big i{font-style:normal;font-weight:700;font-size:20px;display:block}
.giveaway p{position:absolute;left:178px;top:12px;width:200px;font-size:10.5px;line-height:1.35}
.social{position:absolute;left:20px;top:98px;display:flex;gap:60px;font-size:10px}
.social span{display:flex;align-items:center;gap:5px}
.social .dot{background:#fff;border-radius:50%}
.sponsor{position:absolute;left:404px;top:595px;width:200px;height:190px;background:var(--pale);border:3px solid #fff;padding:8px;font-size:10px;font-weight:600;color:var(--blue-dark)}
.art-kittens{position:absolute;left:440px;top:536px;width:160px;height:58px;border-radius:14px;background:linear-gradient(#ffffff,#f5dfe6)}
</style>
</head>
<body>
<main class="flyer">
  <section class="header">
    <div class="scene" role="img" aria-label="Illustrated landscape of hills, grass and clouds"></div>
    <div class="art art-bunny" role="img" aria-label="Illustration of a white bunny peeking over the title"></div>
    <div class="art art-dove" role="img" aria-label="Illustration of a white dove in flight"></div>
    <div class="art art-beagle" role="img" aria-label="Illustration of a beagle dog"></div>
    <div class="art art-goat" role="img" aria-label="Illustration of a brown goat"></div>
    <h1 class="title">Corvel Heights<br>Pet GALA</h1>
    <p class="subtitle">(Fun for Animals In Rescue!)</p>
  </section>
  <svg class="curve" width="618" height="90" viewBox="0 0 618 90" aria-hidden="true">
    <path d="M0 70 Q300 -10 618 40 L618 90 L0 90Z" fill="#f39a1e"/>
    <path d="M0 78 Q300 2 618 48 L618 90 L0 90Z" fill="#2f8a35"/>
    <path d="M0 86 Q300 14 618 56 L618 90 L0 90Z" fill="#f4f4f6"/>
  </svg>
  <div class="date-pill">AUGUST 12, 2018 &nbsp;|&nbsp; SUNDAY &nbsp;|&nbsp; 1:00 - 4:30PM</div>

  <section class="featuring">
    <h2>Animal Education &amp; Adoption Event</h2>
    <p class="sub">featuring:</p>
    <ul>
      <li>BK Pet Shelter &amp; Services</li><li>Featherwell Finches &amp; Larks</li>
      <li>Rabbits &amp; Mice</li><li>Comet Pup Haven</li>
      <li>Hilltop Browsing Sheep</li><li>Marla’s Feline Haven</li>
      <li>Thankful Hounds Haven</li><li>Marvel Pup Haven</li>
    </ul>
  </section>
  <div class="art-dog" role="img" aria-label="Illustration of a brown and white puppy"></div>

  <section class="guest">
    <div class="pig-badge"><div class="pig-art" role="img" aria-label="Illustration of a pink pig"></div></div>
    <div class="guest-text">
      Special Guest from 1:00-3:00PM
      <strong>BeeBop - SF's 1st Therapy Pig!</strong>
      <span class="handle"><i class="dot"></i>@BEEBOP THE HOG</span>
      <span class="handle"><i class="dot"></i>@BEEBOP_BKHOG</span>
    </div>
  </section>

  <section class="tails">
    <span class="tab">Animal Tails</span>
    <div class="rule"></div>
    <ol>
      <li><span class="time">1:00 PM</span>Wendell’s Nook Storytime</li>
      <li><span class="time">1:30 PM</span>BeeBop the Therapy Pig</li>
      <li><span class="time">1:45 PM</span>“Tuft the Saved Hog”</li>
      <li class="note">Read by Author Marnie Oakhurst</li>
      <li><span class="time">2:00 PM</span>Wendell’s Nook Singalong</li>
      <li><span class="time">2:30 PM</span>Featherwell Finch Haven</li>
      <li><span class="time">2:45 PM</span>Quire Pages Storytime</li>
      <li><span class="time">3:00 PM</span>Browsing Sheep Refuge</li>
      <li><span class="time">3:15 PM</span>The Burrow Den Puppet Show</li>
      <li><span class="time">3:45 PM</span>BK PSS Officer Tamsin</li>
      <li><span class="time">4:00 PM</span>Wendell’s Nook Storytime</li>
    </ol>
  </section>

  <section class="kids">
    <span class="tab">Activities for Kids</span>
    <div class="rule"></div>
    <ul>
      <li>Dog &amp; Cat Toy Making with Greta Vossel Canine Coaching</li>
      <li>Animal Mask Making with Tiny Crafters</li>
      <li>Face-in-a-Hole Photo Fun with Hugo Marsh Canine Coaching</li>
    </ul>
  </section>

  <section class="giveaway">
    <div class="big">BK PSS<b>FREE</b><i>Giveaway!</i></div>
    <p>First 75 attending families receive a FREE PSS Doggie Bag containing a dog water bottle, food, shampoo, toy, treats and blinking dog collar light.</p>
    <div class="social">
      <span><i class="dot"></i>Official</span>
      <span><i class="dot"></i>Official</span>
      <span><i class="dot"></i>Official</span>
    </div>
  </section>

  <div class="art-kittens" role="img" aria-label="Illustration of two white kittens peeking over the sponsor box"></div>
  <aside class="sponsor">Sponsored by:</aside>
</main>
</body>
</html>
```